Flyer Design Project

Brindlewick is an IT support company based in the UKl . We protect small busineses from online criminals, malware threats, and technology failure. We do this by creating layers of protection around our clients and their business. We show them the dangers they’re exposed to and how we’ll eliminate them.

We would like to market some special promotions for our managed it services. We want a double sided leaflet , One side will focus on sign up today and get 2 months free it support. On the other we would want to talk about we will not be beaten on price, we offer pro active IT support. Content would need to be along those lines.

I have added a brochure that we have used in the past. Use for ideas.

Industry/Entity Type

Business

```html
<!DOCTYPE html>
<html lang="en">
<head>
<meta charset="utf-8">
<title>Brindlewick – Sign up today</title>
<link rel="stylesheet" href="https://fonts.googleapis.com/css2?family=Arimo:wght@700&family=Tinos:ital,wght@0,700;1,400&display=swap">
<style>
  :root {
    --paper: #ffffff;
    --brand-blue: #1c9ad8;
    --bubble-edge: #2aa7e0;
    --bubble-fill: #9fae6f;
    --bar-green: #6cbf3f;
    --ink: #1b1b1b;
    --copy-grey: #3b3b3b;
    --hero-deep: #13263a;
    --hero-mid: #2f6f9f;
    --hero-light: #7fbfe3;
  }
  html, body {
    margin: 0;
    padding: 0;
    overflow: hidden;
    background: var(--paper);
  }
  .flyer {
    position: relative;
    width: 877px;
    height: 1200px;
    background: var(--paper);
    overflow: hidden;
    font-family: "Arimo", Arial, sans-serif;
  }
  .brand-name {
    position: absolute;
    top: 70px;
    left: 0;
    width: 100%;
    text-align: center;
    margin: 0;
    font-family: "Arimo", Arial, sans-serif;
    font-weight: 700;
    font-size: 72px;
    letter-spacing: -1px;
    color: var(--brand-blue);
  }
  .hero-image {
    position: absolute;
    top: 205px;
    left: 0;
    width: 877px;
    height: 495px;
    background: linear-gradient(180deg, var(--hero-deep) 0%, var(--hero-mid) 65%, var(--hero-light) 100%);
  }
  .hero-rule {
    position: absolute;
    top: 704px;
    left: 0;
    width: 100%;
    height: 2px;
    background: var(--bubble-edge);
  }
  .tagline {
    position: absolute;
    top: 728px;
    left: 0;
    width: 100%;
    margin: 0;
    text-align: center;
    font-weight: 700;
    font-size: 29px;
    line-height: 37px;
    color: var(--copy-grey);
  }
  .offer-bubble {
    position: absolute;
    box-sizing: border-box;
    display: flex;
    flex-direction: column;
    justify-content: center;
    align-items: center;
    background: var(--bubble-fill);
    border: 9px solid var(--bubble-edge);
    border-radius: 70px;
    font-family: "Tinos", "Times New Roman", serif;
    color: var(--ink);
    box-shadow: 4px 6px 8px rgba(0,0,0,0.25);
  }
  .offer-bubble--signup {
    left: 30px;
    top: 845px;
    width: 325px;
    height: 160px;
    font-weight: 700;
    font-size: 54px;
    line-height: 52px;
    align-items: flex-start;
    padding-left: 36px;
  }
  .offer-bubble--free {
    left: 542px;
    top: 928px;
    width: 300px;
    height: 200px;
    font-size: 34px;
    line-height: 35px;
  }
  .offer-bubble__italic { font-style: italic; }
  .offer-bubble__strong { font-weight: 700; font-size: 44px; line-height: 42px; }
  .offer-bubble__support { font-weight: 700; font-size: 37px; line-height: 38px; }
  .ampersand {
    position: absolute;
    left: 372px;
    top: 880px;
    width: 160px;
    text-align: center;
    font-family: "Tinos", "Times New Roman", serif;
    font-weight: 700;
    font-size: 190px;
    line-height: 190px;
    color: var(--ink);
  }
  .footer-rule {
    position: absolute;
    top: 1140px;
    left: 0;
    width: 100%;
    height: 2px;
    background: var(--bubble-edge);
  }
  .call-bar {
    position: absolute;
    top: 1148px;
    left: 0;
    width: 100%;
    height: 52px;
    margin: 0;
    background: var(--bar-green);
    color: var(--paper);
    text-align: center;
    font-weight: 700;
    font-size: 27px;
    line-height: 52px;
  }
</style>
</head>
<body>
  <main class="flyer">
    <h1 class="brand-name">Brindlewick</h1>

    <div class="hero-image" role="img" aria-label="Photo of a digital screen showing a row of padlocks, one of them open"></div>
    <div class="hero-rule"></div>

    <p class="tagline">We protect small businesses from<br>online criminals, malware threats<br>and technology failure</p>

    <div class="offer-bubble offer-bubble--signup">
      <span>Sign up</span>
      <span>today</span>
    </div>

    <div class="ampersand">&amp;</div>

    <div class="offer-bubble offer-bubble--free">
      <span class="offer-bubble__italic">get</span>
      <span class="offer-bubble__italic">2 months</span>
      <span class="offer-bubble__strong">FREE</span>
      <span class="offer-bubble__support">IT support</span>
    </div>

    <div class="footer-rule"></div>
    <p class="call-bar">Call us on : 0871 640 3192 - to schedule your free IT audit</p>
  </main>
</body>
</html>
```